Music Marketing Agency in need of a fully responsive website

Need a website for our music marketing agency with a nice Rev slider has the ability to take payments has a section with our work and client able to see case studies able to download our media kit in PDF can take appointments has social media and a careers upload section. Also want a prominent contact form. Nice and icons for music industry. I want them to be able to download a free Pictagram marketing download Very clean and not large icons or menu at the top very minimal menu bar this will have to go with our logo as well which I will add to order. I want this to be a membership oriented site. so there will be packages displayed or a membership form which they can use to sign up and need a login window. Also need to be able to put Tunevora playlist on the website. Save a section for past clients logos.Again this has to be a clean concept I would like pictures of zPhones such as an app promotion. Definitely want lots of flash words in bold letters across the pages when they scroll through new sections.
Updates

Need extra days to review

Target Market(s)

Urban Music

Coding

Coded - Design and coding required

Font styles to use
Serif

Colors

Designer to choose colors to be used in the design.

Requirements
Must have
• Please Add Logos attached at the Footer

```html
<!DOCTYPE html>
<html lang="en">
<head>
<meta charset="UTF-8">
<title>User Login – Metro Halo Media</title>
<link rel="stylesheet" href="https://fonts.googleapis.com/css2?family=Roboto:wght@400;500&family=Roboto+Condensed:wght@700&display=swap">
<style>
  :root {
    --stage-deep: #7a0a72;
    --stage-mid: #8c1a84;
    --stage-light: #9a3592;
    --panel: #181818;
    --field: #ffffff;
    --field-text: #5a5a5a;
    --accent-green: #62ad45;
    --brand-purple: #8a1c80;
    --text-light: #ffffff;
  }
  * { box-sizing: border-box; margin: 0; padding: 0; }
  html, body {
    width: 1200px;
    height: 600px;
    overflow: hidden;
  }
  body {
    position: relative;
    font-family: "Roboto", Arial, sans-serif;
    color: var(--text-light);
    background: var(--stage-deep);
  }
  .stage-backdrop {
    position: absolute;
    inset: 0;
    background:
      radial-gradient(ellipse at 22% 30%, var(--stage-light) 0%, transparent 45%),
      radial-gradient(ellipse at 78% 40%, var(--stage-light) 0%, transparent 50%),
      linear-gradient(180deg, var(--stage-mid) 0%, var(--stage-deep) 100%);
  }
  .login-panel {
    position: absolute;
    left: 373px;
    top: 77px;
    width: 454px;
    height: 446px;
    background: var(--panel);
    box-shadow: 0 2px 10px rgba(0,0,0,0.35);
  }
  .brand-mark {
    position: absolute;
    left: 0;
    right: 0;
    top: 66px;
    display: flex;
    align-items: center;
    justify-content: center;
    gap: 8px;
    font-family: "Roboto", Arial, sans-serif;
    font-weight: 500;
    font-size: 18px;
    color: var(--text-light);
  }
  .brand-dot {
    width: 14px;
    height: 14px;
    border-radius: 50%;
    background: var(--brand-purple);
  }
  .login-title {
    position: absolute;
    left: 0;
    right: 0;
    top: 147px;
    text-align: center;
    font-family: "Roboto Condensed", "Arial Narrow", sans-serif;
    font-weight: 700;
    font-size: 33px;
    letter-spacing: 0.2px;
  }
  .login-form {
    position: absolute;
    left: 82px;
    top: 209px;
    width: 290px;
  }
  .field {
    display: block;
    width: 100%;
    height: 45px;
    margin-bottom: 15px;
    padding: 0 18px;
    border: none;
    background: var(--field);
    font-family: "Roboto", Arial, sans-serif;
    font-size: 13px;
    color: var(--field-text);
    outline: none;
  }
  .field::placeholder { color: var(--field-text); }
  .login-button {
    display: block;
    width: 100%;
    height: 45px;
    border: none;
    background: var(--accent-green);
    color: var(--text-light);
    font-family: "Roboto Condensed", "Arial Narrow", sans-serif;
    font-weight: 700;
    font-size: 20px;
    cursor: pointer;
  }
  .form-links {
    display: flex;
    justify-content: space-between;
    margin-top: 16px;
    font-size: 12.5px;
  }
  .form-links a { color: var(--text-light); text-decoration: none; }
  .site-footer {
    position: absolute;
    left: 88px;
    top: 561px;
    font-size: 14px;
    display: flex;
    gap: 14px;
  }
  .site-footer a { color: var(--text-light); text-decoration: none; }
</style>
</head>
<body>
  <div class="stage-backdrop" role="img" aria-label="Purple-tinted photo of a concert crowd with raised hands"></div>

  <main class="login-panel">
    <div class="brand-mark"><span class="brand-dot"></span>Metro Halo</div>
    <h1 class="login-title">USER LOGIN</h1>
    <form class="login-form">
      <input class="field" type="text" placeholder="User Name">
      <input class="field" type="password" placeholder="Password">
      <button class="login-button" type="submit">LOG IN</button>
      <div class="form-links">
        <a href="#">Forgot Your Password?</a>
        <a href="#">Sign-Up</a>
      </div>
    </form>
  </main>

  <footer class="site-footer">
    <span>© Copyright 2018 Metro Halo Media</span>
    <span>|</span>
    <a href="#">Privacy Policy.</a>
  </footer>
</body>
</html>
```